Hi Marla,

Hope you are well.

I would like you to Design a Lunch Special poster similar to attachment but use my logo and photos instead ( You can reuse the photos from Zingaroo Platter poster )

I prefer if you can start a new FRESH look for the posters so they don't look too similar as previous.

I like to see more YELLOW colour in the poster this time

Thank you

```html
<!DOCTYPE html>
<html lang="en">
<head>
<meta charset="utf-8">
<title>Lunch Special Flyer</title>
<link href="https://fonts.googleapis.com/css2?family=Barlow:wght@500;600;700&family=Barlow+Condensed:wght@800&display=swap" rel="stylesheet">
<style>
  :root{
    --stage-top:#b9c0c9;
    --stage-bottom:#eef0f2;
    --grey-dark:#7d7d7f;
    --grey-light:#c9c9cb;
    --paper:#f6f6f4;
    --yellow:#e9a83a;
    --purple-top:#a24a92;
    --purple-bottom:#7b44a6;
    --blue:#1d3f8a;
    --ink:#2b2b2b;
    --white:#ffffff;
  }
  *{box-sizing:border-box;margin:0;padding:0}
  html,body{width:1200px;height:800px;overflow:hidden}
  body{
    background:linear-gradient(180deg,var(--stage-top),var(--stage-bottom));
    font-family:"Barlow",sans-serif;
    position:relative;
  }
  .flyer{
    position:absolute;left:340px;top:32px;width:520px;height:736px;
    overflow:hidden;box-shadow:0 10px 30px rgba(0,0,0,.25);
    background:linear-gradient(180deg,var(--grey-dark) 0%,#9a9a9c 55%,var(--grey-light) 100%);
  }
  .flyer-shapes{position:absolute;inset:0}
  .stamp{
    position:absolute;left:42px;top:48px;width:170px;height:170px;border-radius:50%;
    background:radial-gradient(circle,#e9e6e6 0 52%,#b8b3b3 53% 100%);
  }
  .logo-badge{
    position:absolute;left:345px;top:8px;width:150px;height:150px;border-radius:50%;
    background:var(--yellow);display:flex;align-items:center;justify-content:center;
    text-align:center;color:var(--white);
    font-family:"Barlow Condensed",sans-serif;font-weight:800;font-size:40px;line-height:1;
  }
  .hours{
    position:absolute;left:92px;top:282px;color:var(--white);
    font-weight:600;font-size:44px;line-height:1.15;
  }
  .menu-list{
    position:absolute;left:98px;top:398px;list-style:none;color:var(--yellow);
    font-weight:700;font-size:19px;line-height:1.3;
  }
  .price{
    position:absolute;left:350px;top:282px;color:var(--yellow);
    font-family:"Barlow Condensed",sans-serif;font-weight:800;font-size:124px;
    letter-spacing:-2px;line-height:1;
  }
  .photo-card{
    position:absolute;width:156px;height:196px;background:var(--white);padding:10px;
    box-shadow:0 4px 10px rgba(0,0,0,.25);
  }
  .photo-card .photo{width:100%;height:142px}
  .photo-card .label{
    margin-top:8px;background:var(--ink);color:var(--yellow);text-align:center;
    font-weight:600;font-size:16px;padding:6px 0;
  }
  .card-pho{left:28px;top:520px;transform:rotate(-8deg)}
  .card-pho .photo{background:linear-gradient(135deg,#4c5b2c,#c9b27a 55%,#eeeeea)}
  .card-rolls{left:182px;top:500px;transform:rotate(-3deg)}
  .card-rolls .photo{background:linear-gradient(160deg,#d9d6d2,#d6a25a 55%,#b97a32)}
  .card-drink{left:334px;top:486px;transform:rotate(-3deg)}
  .card-drink .photo{background:linear-gradient(90deg,#c8202a 0 45%,#3d8a4a 55%,#e6e6e6)}
</style>
</head>
<body>
  <main class="flyer">
    <svg class="flyer-shapes" viewBox="0 0 520 736" aria-hidden="true">
      <defs>
        <linearGradient id="purpleBlob" x1="0" y1="0" x2="0" y2="1">
          <stop offset="0" stop-color="#a24a92"/>
          <stop offset="1" stop-color="#7b44a6"/>
        </linearGradient>
      </defs>
      <path d="M0 0 H215 Q240 0 244 40 V175 Q244 255 150 262 L0 270 Z" fill="#f6f6f4"/>
      <path d="M420 150 Q520 140 520 200 V600 H390 Q360 500 395 430 Q380 330 345 280 Q325 160 420 150 Z" fill="url(#purpleBlob)"/>
      <path d="M0 520 L120 500 L80 600 L0 610 Z" fill="#1d3f8a"/>
      <path d="M0 670 L160 650 Q210 640 240 660 Q290 700 330 660 L520 620 V736 H0 Z" fill="#e9a83a"/>
    </svg>

    <div class="stamp" role="img" aria-label="Round rubber-stamp badge reading Time for Lunch"></div>
    <div class="logo-badge">YOUR<br>LOGO</div>

    <h1 class="hours">Mon-Fri<br>10am-4pm</h1>
    <ul class="menu-list">
      <li>1x Pho (Any Mains)</li>
      <li>1x Springrools (2 only)</li>
      <li>1x Drink (Soft Drink/Water)</li>
    </ul>
    <div class="price">$15</div>

    <figure class="photo-card card-pho">
      <div class="photo" role="img" aria-label="Photo of a bowl of pho with herbs and chilli"></div>
      <figcaption class="label">PHO</figcaption>
    </figure>
    <figure class="photo-card card-rolls">
      <div class="photo" role="img" aria-label="Photo of crispy spring rolls"></div>
      <figcaption class="label">SPRINGROOLS</figcaption>
    </figure>
    <figure class="photo-card card-drink">
      <div class="photo" role="img" aria-label="Photo of two soft drink cans"></div>
      <figcaption class="label">DRINK</figcaption>
    </figure>
  </main>
</body>
</html>
```